Zestro Design Award - $10,000 tablet app design contest, Retail Catalogue Category

Zestro is a marketplace for Slatebook App Templates (similar to PageForge templates). We want you to design an app template for sale in our marketplace which targets Retail Catalogue Apps (Slatebook Apps that are created for Product Catalogues. For example: paint, clothing… etc).

It’s up to you to create pages or features for the App Template that you think are appropriate. Creativity will be rewarded! Here are some example pages or features that you could create:

• Welcome page
• Features
• Product pages
• Product details
• Share products on Friendlane
• Maps – store locations or events
• Social media integration
• Animations and video

Your design should be Vibrant, Engaging and Contemporary. If you have an Slatebook, download Zestro Lens and download template examples in the download tab.

Your entry must include:
• A brief description of your template
• Preview images of all pages of your template

Attached to this project are free templates to help you get started with your design. We have included:
1. A free portfolio template for designers/photographers
2. Icons and artwork to use in your template
3. Blank pages template
4. Form template
5. Video ad template

If you are selected as a finalist you will be required to submit an .zproject file containing:
• Your LayoutPro source files
• Preview images of your template
• All creative / stock assets used in the template (animations, video etc.)
• A text file with instructions on how to update the template
• A metadata .txt file containing template details and your information

How to enter:
1. Register at Marketplace and view the instructions under the welcome message https://market.zestrobase.example/welcome
2. Download Zestro Builder: https://help.zestrobase.example/entries/48175209-zestro-builder
3. Use the free templates provided in this brief to create your designs and submit to ArtPluvia
Updates

Project Deadline Extended
Reason: Due to the Christmas break we are extending the deadline of our competition. Thank you for time and effort - I will be providing feedback over the next couple of days! Best wishes, Melody

Hi All,

I have received many screenshots with some great designs! I just wanted to clarify that you are designing Zestro app templates including Zestro features and not just page designs?

Read Tips for First Time Zestroers to guide you through the template creation process

Before you start designing templates for Zestro Bazaar

·       Read the Quality Standards

·       Read the Copyright Information 

·       Use the Template Quality Checklist to ensure your template follows our guidelines. 

What should my project file contain?

·       A folder containing your source files, e.g. LayoutPro. This must be named Source.

·       The Zestro content files. This must be named Bundle.

·       Instructions, explaining to a customer how to use your template.

Best wishes,

Melody

Project Deadline Extended
Reason: We are extending the competition by 7 days to give you more time!

Project Deadline Extended
Reason: Due to the lack of submissions to this category we are extending the deadline by 10 days Please let us know if you would like further information on this contest. Best wishes, Melody

Target Market(s)

Entrepreneurs who wish to create Slatebook Apps by using our App design templates.

Industry/Entity Type

Store

Requirements
Must have
• You will need Zestro Builder to open the .zproject files attached to this brief. Get it here: https://help.zestrobase.example/entries/48175209-zestro-builder
Should not have
• • Low quality, fuzzy or blurry images
• Any stock images or content which you do not own the rights to
• Any material which could be considered inappropriate or offensive

```html
<!DOCTYPE html>
<html lang="en">
<head>
<meta charset="utf-8">
<title>Zestro Fashion – Home</title>
<link rel="stylesheet" href="https://fonts.googleapis.com/css2?family=Roboto+Condensed:ital,wght@0,300;0,400;1,300&display=swap">
<style>
  :root {
    --ink: #111111;
    --paper: #ffffff;
    --nav-muted: #7a7a7a;
    --hero-grey: #5e5c60;
    --hero-hair: #8a2a17;
    --hero-warm: #b4442a;
    --band: rgba(205, 205, 205, 0.82);
    --footer: #000000;
    --footer-text: #3a3a3a;
    --social-1: #3b5a8c;
    --social-2: #6fb0cf;
    --social-3: #3d5872;
    --social-4: #7fb6cc;
  }
  * { box-sizing: border-box; margin: 0; padding: 0; }
  html, body {
    width: 921px; height: 1200px; overflow: hidden;
    background: var(--paper);
    font-family: "Roboto Condensed", "Arial Narrow", sans-serif;
    color: var(--ink);
  }
  .app { width: 921px; height: 1200px; display: flex; flex-direction: column; }

  .site-header { height: 146px; background: var(--paper); position: relative; }
  .brand {
    position: absolute; top: 20px; left: 0; right: 0; text-align: center;
    font-size: 22px; font-weight: 300; color: #444;
  }
  .main-nav {
    position: absolute; top: 78px; left: 28px; right: 28px;
    display: flex; justify-content: space-between; align-items: center;
  }
  .main-nav a {
    font-size: 30px; font-weight: 300; color: var(--ink);
    text-decoration: none; padding: 2px 12px; line-height: 38px;
  }
  .main-nav a.is-active { background: var(--ink); color: var(--paper); }
  .main-nav a.is-muted { color: var(--nav-muted); }

  .hero { height: 580px; position: relative; overflow: hidden; }
  .hero-photo {
    position: absolute; inset: 0;
    background:
      radial-gradient(ellipse 38% 55% at 50% 50%, #c7937f 0%, rgba(199,147,127,0) 40%),
      radial-gradient(ellipse 60% 85% at 48% 55%, var(--hero-warm) 0%, var(--hero-hair) 45%, rgba(138,42,23,0) 80%),
      linear-gradient(90deg, #3f3d42 0%, var(--hero-grey) 50%, #8c8a8f 100%);
  }
  .hero-title {
    position: absolute; left: 86px; width: 386px; top: 384px; text-align: center; color: var(--paper);
  }
  .hero-title h1 { font-size: 66px; font-weight: 400; letter-spacing: 1px; line-height: 1; }
  .hero-title .rule { height: 2px; background: rgba(255,255,255,0.75); margin: 12px 0 10px; }
  .hero-title p { font-size: 46px; font-weight: 300; font-style: italic; line-height: 1; }

  .intro { height: 390px; padding: 44px 28px 0; }
  .intro-text {
    font-size: 21px; line-height: 26px; font-weight: 400; padding: 0 12px;
  }
  .intro-text .drop {
    float: left; font-size: 54px; line-height: 44px; font-weight: 300; margin-right: 2px;
  }
  .teasers { display: flex; justify-content: space-between; margin-top: 40px; }
  .teaser { width: 422px; height: 196px; position: relative; overflow: hidden; }
  .teaser-photo { position: absolute; inset: 0; }
  .teaser-photo.collection {
    background:
      radial-gradient(ellipse 22% 55% at 50% 40%, #e9e9e9 0%, rgba(233,233,233,0) 70%),
      linear-gradient(90deg, #5a5a5a 0%, #a9a9a9 50%, #6a6a6a 100%);
  }
  .teaser-photo.arrivals {
    background:
      radial-gradient(ellipse 14% 55% at 50% 60%, #f0eeec 0%, rgba(240,238,236,0) 80%),
      linear-gradient(90deg, #3e3e3e 0%, #9d9d9d 55%, #555555 100%);
  }
  .teaser-label {
    position: absolute; left: 0; right: 0; bottom: 0; height: 54px;
    background: var(--band); padding: 0 8px;
    font-size: 34px; font-weight: 300; line-height: 54px; color: var(--ink);
  }

  .site-footer {
    height: 84px; background: var(--footer);
    display: flex; align-items: center; justify-content: space-between; padding: 0 28px;
  }
  .copyright { font-size: 14px; font-weight: 300; font-style: italic; color: var(--footer-text); }
  .social { display: flex; gap: 20px; }
  .social span { width: 36px; height: 36px; border-radius: 50%; display: block; }
  .social .s1 { background: var(--social-1); }
  .social .s2 { background: var(--social-2); }
  .social .s3 { background: var(--social-3); }
  .social .s4 { background: var(--social-4); }
</style>
</head>
<body>
<div class="app">
  <header class="site-header">
    <div class="brand">[zestro fashion logo]</div>
    <nav class="main-nav">
      <a href="#" class="is-active">HOME</a>
      <a href="#">COLLECTION</a>
      <a href="#">PRODUCTS</a>
      <a href="#" class="is-muted">PRESS</a>
      <a href="#" class="is-muted">ABOUT</a>
      <a href="#" class="is-muted">CONTACT</a>
    </nav>
  </header>

  <section class="hero">
    <div class="hero-photo" role="img" aria-label="Fashion portrait of a model with long voluminous red hair against a grey studio backdrop"></div>
    <div class="hero-title">
      <h1>ZESTRO</h1>
      <div class="rule"></div>
      <p>fall/winter 2013</p>
    </div>
  </section>

  <main class="intro">
    <p class="intro-text"><span class="drop">C</span>upcake ipsum dolor sit amet jujubes sesame snaps I love apple pie. Sweet I love wafer. Candy donut gummi bears applicake faworki caramels I love dragée. Ice cream pastry cotton candy marzipan lemon drops.</p>
    <div class="teasers">
      <a class="teaser" href="#">
        <div class="teaser-photo collection" role="img" aria-label="Black and white portrait of a blonde model with wavy hair"></div>
        <div class="teaser-label">explore the latest collection &gt;</div>
      </a>
      <a class="teaser" href="#">
        <div class="teaser-photo arrivals" role="img" aria-label="Model in a white draped outfit with a sculpted updo on a grey backdrop"></div>
        <div class="teaser-label">latest arrivals &gt;</div>
      </a>
    </div>
  </main>

  <footer class="site-footer">
    <span class="copyright">(c) zestro fashion 2013</span>
    <div class="social" aria-label="Social links">
      <span class="s1"></span><span class="s2"></span><span class="s3"></span><span class="s4"></span>
    </div>
  </footer>
</div>
</body>
</html>
```